Label Design for Exciting Range of Nutritional Supplements

We are looking for a bright, modern design for a new range of food supplements under our new brand.

The label needs to convey a premium, high quality product with a vibrant picture of fresh fruit and clear text of what the product is.

The label needs to have a prominent colour, which matches the fruit contained in the supplement. e.g. Rasberry Ketone would have rasberry colour prominent on the label.

The chosen label will act as a template for the other labels in the range. To create the other labels, the main text can be changed and the picture of the fruit changed and the main colour altered to match the fruit.

We love the designs here: http://qzlink.example/7RvTkwp BUT our label design must not be seen to be a copy of these, they are trademarked, but must be of a unique design. I thought of the fruit morphing into a liquid drop shape dripping into a capsule to convey the fruit is contained in the capsule, but I am not sure if this would be too difficult?

Perhaps the ovel shape on our logo could encircle the label? Just ideas, I'm wide open to suggestions.

The main thing is that the label is bright, modern and attractive.

The label will wrap around a cylindrical bottle. The label size is 150mm x 72mm. The main 'focus' of the front of the logo is approximately 65mm wide in the middle of the label.

I have attached our logo in .ai and .png format. Our logo should be on the label, but we are hoping to have the label on the cap so it does not need to be too prominent on the label.

Initially the requirement is for one label: Rasberry Ketone

If the fiorst label is good, we will also require:

Garcinia Cambogia
Green Coffee
Acai Berry
African Mango

So the initial label should be the template for the others.

We will require more label designs for further products in the future.

Deliverables will need to be in Photoshop or Adobe Illustrator or Fireworks (or all three!)

```html
<!DOCTYPE html>
<html lang="en">
<head>
<meta charset="utf-8">
<title>Raspberry Ketone – Supplement Label</title>
<link href="https://fonts.googleapis.com/css2?family=Raleway:wght@200;300&family=Arimo:wght@400;700&display=swap" rel="stylesheet">
<style>
  :root {
    --brand-blue: #2b8ef2;
    --berry: #e0115f;
    --berry-soft: #f7c9da;
    --paper: #ffffff;
    --canvas: #f2f2f4;
    --fruit-red: #d9223a;
    --fruit-dark: #9e0f22;
  }
  html, body {
    margin: 0;
    width: 1200px;
    height: 1000px;
    overflow: hidden;
    background: var(--canvas);
  }
  .label {
    position: absolute;
    left: 50px;
    top: 236px;
    width: 1100px;
    height: 528px;
    background: var(--paper);
    overflow: hidden;
    box-shadow: 0 6px 24px rgba(0,0,0,0.12);
  }
  .band-top {
    position: absolute;
    left: 0; top: 0;
    width: 100%; height: 64px;
    background: var(--brand-blue);
  }
  .brand {
    position: absolute;
    right: 250px; top: 18px;
    display: flex;
    align-items: center;
    gap: 8px;
    font-family: "Arimo", Arial, sans-serif;
    font-weight: 700;
    font-size: 24px;
    line-height: 28px;
    color: var(--paper);
  }
  .brand-dot {
    width: 14px; height: 14px;
    border-radius: 50%;
    background: var(--paper);
  }
  .band-title {
    position: absolute;
    left: 0; top: 64px;
    width: 100%; height: 92px;
    background: var(--berry);
  }
  .title {
    position: absolute;
    left: 300px;
    margin: 0;
    font-family: "Raleway", sans-serif;
    font-weight: 200;
    font-size: 88px;
    line-height: 1;
    letter-spacing: -1px;
    text-transform: uppercase;
  }
  .title-main { top: 66px; color: var(--berry-soft); }
  .title-sub { top: 158px; color: var(--berry); }
  .ingredients {
    position: absolute;
    left: 300px; top: 300px;
    margin: 0; padding: 0;
    list-style: none;
    font-family: "Arimo", Arial, sans-serif;
    font-size: 21px;
    line-height: 25px;
    color: var(--brand-blue);
  }
  .ingredients li::before {
    content: "•";
    font-size: 12px;
    vertical-align: 4px;
    margin-right: 6px;
  }
  .fruit-photo {
    position: absolute;
    left: 600px; top: 244px;
    width: 200px; height: 178px;
  }
  .food-supplement {
    position: absolute;
    right: 330px; top: 432px;
    font-family: "Arimo", Arial, sans-serif;
    font-size: 19px;
    line-height: 22px;
    color: var(--berry);
  }
  .band-bottom {
    position: absolute;
    left: 0; bottom: 0;
    width: 100%; height: 64px;
    background: var(--berry);
  }
  .capsule-count {
    position: absolute;
    left: 300px; top: 470px;
    padding: 5px 14px;
    border-radius: 16px;
    background: var(--paper);
    font-family: "Arimo", Arial, sans-serif;
    font-size: 11px;
    line-height: 16px;
    color: var(--berry);
    text-transform: uppercase;
  }
  .capsule-count strong { font-size: 14px; margin-right: 2px; }
</style>
</head>
<body>
  <div class="label">
    <div class="band-top"></div>
    <div class="brand"><span class="brand-dot"></span>Lumora Health</div>

    <div class="band-title"></div>
    <h1 class="title title-main">Raspberry</h1>
    <p class="title title-sub">Ketone</p>

    <ul class="ingredients">
      <li>Raspberry Ketones</li>
      <li>Pure Caffeine</li>
      <li>Reservatrol</li>
      <li>Lumora Blend</li>
    </ul>

    <svg class="fruit-photo" viewBox="0 0 200 178" role="img" aria-label="Photograph of fresh raspberries with green leaves">
      <defs>
        <radialGradient id="berry-tone" cx="45%" cy="45%" r="60%">
          <stop offset="0%" stop-color="#d9223a"/>
          <stop offset="100%" stop-color="#9e0f22"/>
        </radialGradient>
      </defs>
      <ellipse cx="100" cy="92" rx="95" ry="80" fill="url(#berry-tone)" opacity="0.85"/>
    </svg>

    <div class="food-supplement">Food Supplement</div>
    <div class="band-bottom"></div>
    <div class="capsule-count"><strong>90</strong>Capsules</div>
  </div>
</body>
</html>
```